Night Dresses business cards business requirers

We are a new company initiating Mexico operations. Our core business is Night woman dress (both formal and party dress) for rent. Gownhaven is the name of the company. ITS Gownhaven form by two word. The dress word and topia (Utopic) so the place Gownhaven Means That You cant get the ideal, perfect and unique dress for your event. So we would like a modern, very creative, and attractive business card.

Industry/Entity Type

Womens Clothing

Contact Information for Business Card

Rounded Borders, two faces

Requirements
Must have
• Rounded borders, logo and slogan, modern, glam, attractive design
Should not have
• modern design classic or not

```html
<!DOCTYPE html>
<html lang="en">
<head>
<meta charset="UTF-8">
<title>Gownhaven Business Card</title>
<link href="https://fonts.googleapis.com/css2?family=Open+Sans:wght@400;600;700&display=swap" rel="stylesheet">
<style>
  :root {
    --backdrop: #3e3637;
    --card: #ffffff;
    --brand: #b0559b;
    --ink: #2b2b2b;
    --ink-soft: #3a3a3a;
  }
  * { margin: 0; padding: 0; box-sizing: border-box; }
  html, body {
    width: 1200px;
    height: 1000px;
    overflow: hidden;
    background: var(--backdrop);
    font-family: "Open Sans", Arial, sans-serif;
  }
  .card {
    position: absolute;
    width: 560px;
    height: 320px;
    background: var(--card);
    border-radius: 22px;
    box-shadow: 0 10px 30px rgba(0,0,0,0.35);
  }
  .card--front { left: 80px; top: 110px; }
  .card--back { left: 560px; top: 570px; }

  /* Front face */
  .brand-lockup {
    position: absolute;
    left: 0;
    right: 0;
    top: 118px;
    display: flex;
    align-items: center;
    justify-content: center;
    gap: 18px;
  }
  .brand-square {
    width: 22px;
    height: 22px;
    background: var(--brand);
    flex: none;
  }
  .brand-text { display: flex; flex-direction: column; align-items: center; }
  .brand-name {
    color: var(--brand);
    font-size: 40px;
    font-weight: 400;
    letter-spacing: 7px;
    line-height: 1;
  }
  .brand-slogan {
    margin-top: 8px;
    color: var(--ink-soft);
    font-size: 17px;
    letter-spacing: 5px;
  }

  /* Back face */
  .person {
    position: absolute;
    left: 56px;
    top: 132px;
    width: 196px;
    text-align: right;
  }
  .person-name {
    color: var(--brand);
    font-size: 30px;
    font-weight: 700;
    line-height: 1;
    white-space: nowrap;
  }
  .person-role {
    color: var(--ink);
    font-size: 15px;
    font-weight: 600;
    margin-top: 4px;
  }
  .contact-list {
    position: absolute;
    left: 296px;
    top: 70px;
    list-style: none;
  }
  .contact-list li {
    display: flex;
    align-items: center;
    gap: 10px;
    color: var(--ink);
    font-size: 15px;
    line-height: 20px;
    white-space: nowrap;
  }
  .contact-list svg { width: 13px; height: 13px; fill: var(--brand); flex: none; }
  .contact-list .accent { color: var(--brand); }
  .address {
    position: absolute;
    left: 236px;
    top: 262px;
    display: flex;
    align-items: center;
    gap: 10px;
    color: var(--ink);
    font-size: 15px;
    white-space: nowrap;
  }
  .address svg { width: 15px; height: 15px; fill: var(--brand); flex: none; }
</style>
</head>
<body>

<section class="card card--front">
  <div class="brand-lockup">
    <div class="brand-square"></div>
    <div class="brand-text">
      <div class="brand-name">GOWNHAVEN</div>
      <div class="brand-slogan">GOWNS ON LOAN</div>
    </div>
  </div>
</section>

<section class="card card--back">
  <div class="person">
    <div class="person-name">ELENA WARD</div>
    <div class="person-role">CEO/FOUNDER</div>
  </div>

  <ul class="contact-list">
    <li>
      <svg viewBox="0 0 16 16"><path d="M4 1l3 3-2 2c1 2 3 4 5 5l2-2 3 3-2 3C7 15 1 9 1 3z"/></svg>
      000 000 0000
    </li>
    <li>
      <svg viewBox="0 0 16 16"><rect x="1" y="6" width="14" height="8" rx="1"/><rect x="4" y="1" width="8" height="4"/></svg>
      000 000 0000
    </li>
    <li>
      <svg viewBox="0 0 16 16"><path d="M1 3h14v10H1z M1 3l7 6 7-6" stroke="#fff" stroke-width="1"/></svg>
      info@elenaward.com
    </li>
    <li>
      <svg viewBox="0 0 16 16"><circle cx="9" cy="7" r="5" fill="none" stroke="#b0559b" stroke-width="2.2"/><path d="M5.5 10.5L1 15" stroke="#b0559b" stroke-width="2.4"/></svg>
      <span>www.<span class="accent">yoursitename</span>.com</span>
    </li>
  </ul>

  <div class="address">
    <svg viewBox="0 0 16 16"><path d="M15 1L1 7l6 2 2 6z"/></svg>
    Your Street address, Singapore-1200
  </div>
</section>

</body>
</html>
```